Roofing company franchise truck wrap design

Design a truck wrap that is bold, noticeable and eye catching using the words from my logo and my new mascot as the center of the design, along with the original logo icon. Note that the blue and green from the original logo have been altered. Use the new colors.

Sides of the truck should be bold, as sample. Background of lightning, storm or black matte steel coloring preferred with bold strokes of strategic color. Logo icon on hood. Back of tailgate and window more informational than sides. Keep sides bold and easily seen.

Side of truck. The words Gable and Steady from logo. ".com" entered by name instead of full web address again. Slogan, "A brighter path to shelter" on sides. Number of "844-TILE555" on sides.

Full name, web address, services, phone number, etc. on back of tailgate and window. Mascot somewhere on back as well.

See updated images. Truck is a bison 2200 not a kestrel or van. Use colors from new logo. Several have used the wrong colors.
Updates

Updated a quick mock up of what I had in mind. Also, a bunch of wraps I've seen that I like. Remember to adjust the blue and green to the new colors. The original .ai colors are incorrect.

I really like the cartoony looking weather/ storm/ lightning look on the one truck. Looking for blog and noticeable but fun and rememberable.

Some great designs. Thanks everyone. If I could add some notes, make it more "cartoonish." For instance, make the "flat" black background with the lightning/ storm more cartoon looking. I really like that background used in conjunction with the blue and green colors and flat black without storm used strategically. I really like the use of the logo in the background, both behind the mascot and as background or throughout design. My truck is blacked out, so please make rims and grills black, not chrome.

Thanks again.

Still waiting for some revisions to be completed and there's been a few new entries that need reviewed. Will private message those being considered. Or already have and are waiting for revisions before deciding.

I’m down to two designers. Thanks for all your work. I’ll decide on final choice as soon as receiving last revisions. I’ll then Work specifically to finalize any wording or slight changes needed.

Target Market(s)

Home and property owners

Industry/Entity Type

Roofing business franchise

Font styles to use
Other font styles liked:
• See images. Font for logo and “a brighter path to shelter can be like hand written similar to like my quick mockup and inspiration images. Font does not need to be one shown.

Requirements
Must have
• Bold clean design. Powerful message
Nice to have
• See inspiration pictures and my quick mockup. Images added

```html
<!DOCTYPE html>
<html lang="en">
<head>
<meta charset="UTF-8">
<title>Gable Steady – Truck Side Wrap</title>
<link rel="stylesheet" href="https://fonts.googleapis.com/css2?family=Oswald:wght@700&family=Montserrat:wght@700;800&display=swap">
<style>
  :root {
    --page-bg: #f2f2f0;
    --wrap-brown: #8a4a1c;
    --wrap-brown-deep: #6b3512;
    --wrap-white: #ffffff;
    --streak-gold: #e0a42a;
    --streak-amber: #c9801f;
    --brand-blue: #1a2fd6;
    --brand-green: #3fae2a;
    --phone-white: #ffffff;
  }
  html, body {
    margin: 0;
    padding: 0;
    width: 1200px;
    height: 1200px;
    overflow: hidden;
    background: var(--page-bg);
  }
  .canvas {
    position: relative;
    width: 1200px;
    height: 1200px;
  }
  .side-panel {
    position: absolute;
    left: 40px;
    top: 185px;
    width: 1120px;
    height: 830px;
    overflow: hidden;
    box-shadow: 0 4px 18px rgba(0,0,0,0.15);
  }
  .panel-art {
    position: absolute;
    inset: 0;
    width: 1120px;
    height: 830px;
  }
  .brand-square {
    position: absolute;
    left: 78px;
    top: 62px;
    width: 92px;
    height: 92px;
    background: var(--brand-green);
    border-radius: 10px;
  }
  .phone-number {
    position: absolute;
    right: 44px;
    top: 70px;
    margin: 0;
    font-family: "Montserrat", sans-serif;
    font-weight: 800;
    font-size: 56px;
    letter-spacing: 1px;
    color: var(--phone-white);
  }
  .wordmark {
    position: absolute;
    left: 52px;
    top: 360px;
    margin: 0;
    font-family: "Oswald", sans-serif;
    font-weight: 700;
    color: var(--brand-blue);
    line-height: 0.95;
    text-transform: uppercase;
  }
  .wordmark-top {
    display: block;
    font-size: 168px;
    letter-spacing: 2px;
  }
  .wordmark-bottom {
    display: block;
    font-size: 118px;
    letter-spacing: 1px;
  }
  .wordmark-domain {
    font-size: 58px;
    text-transform: lowercase;
    letter-spacing: 1px;
    margin-left: 10px;
  }
  .slogan {
    position: absolute;
    left: 56px;
    top: 668px;
    margin: 0;
    font-family: "Montserrat", sans-serif;
    font-weight: 800;
    font-size: 34px;
    letter-spacing: 3px;
    color: var(--brand-blue);
    text-transform: uppercase;
  }
  .mascot-area {
    position: absolute;
    left: 760px;
    top: 230px;
    width: 310px;
    height: 540px;
    border-radius: 150px 150px 40px 40px;
    background: linear-gradient(180deg, #b5723c 0%, #9a5a2a 45%, #2a3a8a 75%, #c98b2c 100%);
  }
</style>
</head>
<body>
<main class="canvas">
  <section class="side-panel">
    <svg class="panel-art" viewBox="0 0 1120 830" xmlns="http://www.w3.org/2000/svg" aria-hidden="true">
      <defs>
        <linearGradient id="brownField" x1="0" y1="0" x2="1" y2="1">
          <stop offset="0" stop-color="var(--wrap-brown)"/>
          <stop offset="1" stop-color="var(--wrap-brown-deep)"/>
        </linearGradient>
      </defs>
      <rect class="brown-field" width="1120" height="830" fill="url(#brownField)"/>
      <path class="corner-sweep" d="M0,0 H440 C350,120 190,205 0,235 Z" fill="var(--wrap-white)"/>
      <path class="gold-streak" d="M430,0 C560,150 820,250 1120,270" fill="none" stroke="var(--streak-gold)" stroke-width="18"/>
      <path class="amber-streak" d="M470,0 C610,130 840,215 1120,225" fill="none" stroke="var(--streak-amber)" stroke-width="8"/>
      <path class="gold-streak-low" d="M560,300 C760,330 920,360 1120,470" fill="none" stroke="var(--streak-gold)" stroke-width="10"/>
      <path class="main-sweep" d="M0,300 C350,232 790,250 1090,380 C870,430 770,700 560,768 C380,800 150,792 0,792 Z" fill="var(--wrap-white)"/>
    </svg>

    <div class="brand-square"></div>
    <p class="phone-number">844-TILE555</p>

    <h1 class="wordmark">
      <span class="wordmark-top">Gable</span>
      <span class="wordmark-bottom">Steady<span class="wordmark-domain">.com</span></span>
    </h1>
    <p class="slogan">A brighter path to shelter</p>

    <div class="mascot-area" role="img" aria-label="Cartoon dog mascot in work boots and a branded shirt, holding a nail gun and giving a thumbs up, with a speech bubble"></div>
  </section>
</main>
</body>
</html>
```